Debt Relief Landing Page Design

I need a landing page designed (and the accompanying Thank You page) for my client.

I have drafted the wireframes for the layout of the pages (attached) and need a professional looking finish.

The main colours to use are green and blue as per their current branding, see website for specifications - http://www.clearpathledger.com.au/

```html
<!DOCTYPE html>
<html lang="en">
<head>
<meta charset="utf-8">
<title>Clear Path Ledger – Debt Relief</title>
<link href="https://fonts.googleapis.com/css2?family=Roboto:ital,wght@0,400;0,500;0,700;1,400&display=swap" rel="stylesheet">
<style>
:root{
  --green:#4d7f1f;
  --green-dark:#3c6617;
  --green-text:#4a8a1c;
  --navy:#13203d;
  --text:#555;
  --line:#e4e4e4;
  --footer:#e6e6e6;
  --white:#fff;
}
*{margin:0;padding:0;box-sizing:border-box}
html,body{width:692px;height:1200px;overflow:hidden;background:var(--white)}
body{font-family:'Roboto',Arial,sans-serif;color:var(--text);position:relative}
.abs{position:absolute}
.top-rule{left:0;top:0;width:692px;height:2px;background:var(--green)}
.brand{left:57px;top:28px;font-size:20px;font-weight:500;color:var(--navy);letter-spacing:-.3px;display:flex;align-items:center;gap:6px}
.brand-dot{width:10px;height:10px;border-radius:50%;background:var(--green)}
.contact{left:514px;top:22px}
.contact-label{font-size:8px;font-weight:700;color:var(--navy)}
.contact-phone{font-size:21px;font-weight:700;color:var(--green);line-height:24px}
.header-rule{left:0;top:78px;width:692px;height:1px;background:var(--green)}
.hero{left:0;top:79px;width:692px;height:278px;background:linear-gradient(90deg,#e9ecef 0%,#f3f4f5 35%,#dde0e4 70%,#c9c4c6 100%)}
.hero-photo{left:252px;top:79px;width:202px;height:278px;background:linear-gradient(180deg,#d9c89a 0%,#e8d8c4 35%,#8e93d6 65%,#7f86cf 100%)}
.hero-title{left:57px;top:119px;font-size:21px;font-weight:500;color:var(--navy)}
.hero-title-big{left:57px;top:143px;font-size:32px;font-weight:700;color:var(--green)}
.hero-sub{left:57px;top:189px;width:240px;font-size:12.5px;line-height:16px;color:var(--navy)}
.hero-copy{left:57px;top:237px;width:215px;font-size:7px;line-height:12px;color:#333}
.btn-read{left:57px;top:291px;width:54px;height:22px;background:var(--navy);color:var(--white);font-size:6.5px;display:flex;align-items:center;justify-content:center}
.dots{left:324px;top:325px;display:flex;gap:3px;align-items:center}
.dots span{width:7px;height:7px;border-radius:50%;background:var(--white)}
.dots .on{width:11px;height:11px;border:2px solid var(--white);background:transparent}
.form-panel{left:454px;top:69px;width:180px;height:299px;background:var(--green)}
.flare{fill:var(--green-dark)}
.form-title{left:454px;top:73px;width:180px;text-align:center;font-size:18px;font-weight:500;color:var(--white)}
.form-note{left:454px;top:100px;width:180px;text-align:center;font-size:6.5px;line-height:11px;color:var(--white)}
.field-label{left:461px;font-size:6.5px;line-height:9px;color:var(--white)}
.field{left:500px;width:124px;height:26px;background:var(--white);border-radius:2px}
.btn{display:flex;align-items:center;justify-content:center;color:var(--white);font-weight:500;border-radius:2px}
.btn-form{left:462px;top:328px;width:163px;height:28px;background:var(--navy);font-size:10.5px}
.section-title{left:0;width:692px;text-align:center;font-size:21px;font-weight:500;color:var(--navy)}
.service{width:200px;text-align:center}
.service-icon{width:64px;height:64px;border-radius:50%;background:var(--green);margin:0 auto;display:flex;align-items:center;justify-content:center}
.service-icon.navy{background:var(--navy)}
.service-name{margin-top:11px;font-size:10px;font-weight:500;color:var(--green-text)}
.service-name.navy{color:var(--navy)}
.service-desc{margin-top:5px;font-size:7px;line-height:10.5px;color:var(--text)}
.btn-navy{left:265px;top:726px;width:163px;height:28px;background:var(--navy);font-size:10.5px}
.divider{left:57px;top:783px;width:578px;height:1px;background:var(--line)}
.quote{width:185px}
.quote-mark{position:absolute;left:0;top:-6px;font-size:38px;font-family:Georgia,serif;color:#cfcfcf;line-height:1}
.quote-text{margin-left:27px;font-size:7px;font-style:italic;line-height:12px;color:#555}
.quote-by{margin-left:27px;margin-top:9px;font-size:8px;color:#555}
.quote-by b{font-weight:400;color:var(--green-text)}
.btn-green{left:265px;top:1096px;width:163px;height:27px;background:var(--green);font-size:10.5px}
.footer{left:0;top:1149px;width:692px;height:51px;background:var(--footer)}
.social{left:57px;top:1167px;display:flex;gap:2px}
.social span{width:18px;height:18px;border-radius:50%;background:#b9b9b9}
.social .active{background:var(--green)}
.legal{right:57px;top:1170px;font-size:6.5px;color:#555}
</style>
</head>
<body>
<div class="abs top-rule"></div>

<header>
  <div class="abs brand"><span class="brand-dot"></span>Clear Path Ledger</div>
  <div class="abs contact">
    <div class="contact-label">CONTACT US ON</div>
    <div class="contact-phone">1300 555 014</div>
  </div>
</header>
<div class="abs header-rule"></div>

<section class="hero-section">
  <div class="abs hero" role="img" aria-label="Softly blurred bright office background"></div>
  <div class="abs hero-photo" role="img" aria-label="Photo of a smiling woman in a light blue shirt"></div>
  <h1 class="abs hero-title">Looking To Consolidate</h1>
  <div class="abs hero-title-big">Your Debts?</div>
  <p class="abs hero-sub">If You Have Over $10,000 In Debt, We Can Help You Be Debt Free In 3-5 Years.</p>
  <p class="abs hero-copy">Ledger Advisors is Australia's debt help relief specialists. Through years of industry experience and knowledge, our team of debt management experts can actively advise you on how to get out of the red, fast.</p>
  <div class="abs btn-read">READ MORE</div>
  <div class="abs dots"><span></span><span></span><span class="on"></span><span></span></div>

  <svg class="abs" style="left:440px;top:69px" width="208" height="300" viewBox="0 0 208 300">
    <polygon class="flare" points="14,0 4,10 14,10"/>
    <polygon class="flare" points="194,0 204,10 194,10"/>
    <polygon class="flare" points="14,288 0,288 14,300"/>
    <polygon class="flare" points="194,288 208,288 194,300"/>
  </svg>
  <div class="abs form-panel"></div>
  <div class="abs form-title">Free Consultation</div>
  <div class="abs form-note">FILL IN THE FORM BELOW TO RECEIVE<br>YOUR FREE, NO OBLIGATION CONSULTATION</div>
  <div class="abs field-label" style="top:151px">Name:</div><div class="abs field" style="top:141px"></div>
  <div class="abs field-label" style="top:180px">Phone:</div><div class="abs field" style="top:170px"></div>
  <div class="abs field-label" style="top:210px">Email:</div><div class="abs field" style="top:200px"></div>
  <div class="abs field-label" style="top:240px">Postcode:</div><div class="abs field" style="top:230px"></div>
  <div class="abs field-label" style="top:265px">Unsecured<br>Debt:</div><div class="abs field" style="top:261px"></div>
  <div class="abs field-label" style="top:295px">Preferred<br>Call Time:</div><div class="abs field" style="top:291px"></div>
  <div class="abs btn btn-form">GET MY FREE CONSULTATION</div>
</section>

<section class="services">
  <h2 class="abs section-title" style="top:390px">Here Are Just Some Of Our Debt Relief Services</h2>

  <div class="abs service" style="left:38px;top:447px">
    <div class="service-icon"><svg width="26" height="28" viewBox="0 0 26 28"><path d="M9 2h8l-3 5h-2z" fill="#fff"/><path d="M11 7h4c6 3 9 9 9 14 0 4-3 6-11 6S2 25 2 21c0-5 3-11 9-14z" fill="#fff"/><text x="13" y="23" text-anchor="middle" font-size="11" font-weight="700" fill="#4d7f1f" font-family="Roboto,sans-serif">$</text></svg></div>
    <div class="service-name">Debt Consolidation Loans</div>
    <div class="service-desc">Stop getting hassled by creditors. Let us consolidate<br>your personal debts into an easy repayment plan</div>
  </div>
  <div class="abs service navy-svc" style="left:246px;top:447px">
    <div class="service-icon navy"><svg width="28" height="24" viewBox="0 0 28 24"><path d="M14 1L1 12h4v11h18V12h4z" fill="#fff"/><text x="14" y="20" text-anchor="middle" font-size="12" font-weight="700" fill="#13203d" font-family="Roboto,sans-serif">$</text></svg></div>
    <div class="service-name navy">Mortgage Refinance</div>
    <div class="service-desc">Consolidate your debt into available home loan equity,<br>significantly reducing your general repayments</div>
  </div>
  <div class="abs service" style="left:454px;top:447px">
    <div class="service-icon"><svg width="28" height="20" viewBox="0 0 28 20"><rect x="1" y="1" width="26" height="18" rx="3" fill="#fff"/><rect x="1" y="6" width="26" height="3" fill="#4d7f1f"/><rect x="4" y="12" width="20" height="1.5" fill="#4d7f1f"/></svg></div>
    <div class="service-name">Debt Agreements</div>
    <div class="service-desc">A viable alternative to Bankruptcy and debt<br>consolidation loans.</div>
  </div>

  <div class="abs service" style="left:38px;top:579px">
    <div class="service-icon"><svg width="34" height="26" viewBox="0 0 34 26"><rect x="7" y="2" width="26" height="16" rx="2" fill="none" stroke="#fff" stroke-width="2"/><rect x="7" y="6" width="26" height="2.5" fill="#fff"/><rect x="22" y="11" width="8" height="4" rx="2" fill="#fff"/><rect x="1" y="14" width="11" height="10" rx="1" fill="#fff"/><path d="M3.5 14v-3a3 3 0 0 1 6 0v3" fill="none" stroke="#fff" stroke-width="2"/></svg></div>
    <div class="service-name">Credit Repair</div>
    <div class="service-desc">Assist you in removing unfair, disputable and incorrect<br>information from your credit file, information which you<br>believe should not be there.</div>
  </div>
  <div class="abs service" style="left:246px;top:579px">
    <div class="service-icon"><svg width="28" height="26" viewBox="0 0 28 26"><path d="M14 1L2 7v2h24V7z" fill="#fff"/><rect x="5" y="11" width="3" height="10" fill="#fff"/><rect x="10.5" y="11" width="3" height="10" fill="#fff"/><rect x="16" y="11" width="3" height="10" fill="#fff"/><rect x="21" y="11" width="3" height="10" fill="#fff"/><rect x="2" y="22" width="24" height="3" fill="#fff"/></svg></div>
    <div class="service-name">Bankruptcy</div>
    <div class="service-desc">We will work with you to accurately determine if<br>Bankruptcy is the sole option for your situation.</div>
  </div>
  <div class="abs service" style="left:454px;top:579px">
    <div class="service-icon"><svg width="30" height="24" viewBox="0 0 30 24"><rect x="2" y="6" width="22" height="15" rx="2" fill="#fff" transform="rotate(-8 13 13)"/><rect x="7" y="3" width="22" height="15" rx="2" fill="#fff" stroke="#4d7f1f" stroke-width="1.2"/><rect x="7" y="6.5" width="22" height="2.5" fill="#4d7f1f"/><circle cx="24" cy="13" r="2" fill="#4d7f1f"/></svg></div>
    <div class="service-name">Bad Credit Loans</div>
    <div class="service-desc">Work in your best interests to provide a consolidation<br>loan that turns your bad credit history into a positive<br>financial situation</div>
  </div>

  <div class="abs btn btn-navy">GET MY FREE CONSULTATION</div>
</section>

<div class="abs divider"></div>

<section class="testimonials">
  <h2 class="abs section-title" style="top:802px">Here's What Our Valued Customers Have To Say About Us</h2>

  <div class="abs quote" style="left:57px;top:858px">
    <span class="quote-mark">“</span>
    <p class="quote-text">We were on the verge of losing our car and did not know what to do but now we are in an affordable arrangement to catch up our car payments and are on our way to a debt free future. We are even thinking of buying a house, without your help this would not be possible</p>
    <p class="quote-by"><b>Margaret Box Hill</b>, VIC</p>
  </div>
  <div class="abs quote" style="left:258px;top:858px">
    <span class="quote-mark">“</span>
    <p class="quote-text">I am writing this letter to express my appreciation for all your help with sorting my finances out. My consultant worked through an easy to understand payment plan which I can easily afford and understand. Thank you</p>
    <p class="quote-by"><b>Peter, Liverpool</b>, NSW</p>
  </div>
  <div class="abs quote" style="left:461px;top:858px">
    <span class="quote-mark">“</span>
    <p class="quote-text">I am very relieved and can now get my life on track. I very sincerely appreciate all of your assistance. You treated me like a person and never condemned me for the situation I was in. If ever I have the opportunity to recommend your services, I will sincerely recommend you.</p>
    <p class="quote-by"><b>Leah, Howlong</b>, NSW</p>
  </div>

  <div class="abs quote" style="left:57px;top:977px">
    <span class="quote-mark">“</span>
    <p class="quote-text">The previous finance company I went to couldn't consolidate all my debt so put me in worse position. Ledger Advisors stepped in, I am now making only one payment and it saves me $500 per month</p>
    <p class="quote-by"><b>Doonside</b>, NSW</p>
  </div>
  <div class="abs quote" style="left:258px;top:977px">
    <span class="quote-mark">“</span>
    <p class="quote-text">I had lost my job and my creditors were about to take legal action against me. I had no idea of what options I had and thought I was going to lose everything I had worked so hard for. With your help I was able to work out a payment arrangement that everyone I owed money to accepted.</p>
    <p class="quote-by"><b>Tom, Penrith</b>, NSW</p>
  </div>
  <div class="abs quote" style="left:461px;top:977px">
    <span class="quote-mark">“</span>
    <p class="quote-text">Thank you so much for helping me so quickly with my finances. All the credit agencies have stopped calling and I can live a normal life hassle free</p>
    <p class="quote-by"><b>Rachel, Hoppers Crossing</b>, VIC</p>
  </div>

  <div class="abs btn btn-green">GET MY FREE CONSULTATION</div>
</section>

<footer>
  <div class="abs footer"></div>
  <div class="abs social"><span></span><span></span><span class="active"></span><span></span></div>
  <div class="abs legal">© 2015 Clear Path Ledger. All rights reserved &nbsp;Privacy Policy &nbsp;Terms &amp; Conditions</div>
</footer>
</body>
</html>
```